Qorda - Web Design Rebrand for Talent Resourcing Company

I need a new brand for a customer based in Ireland.
The website currently: https://brevantic.io/
Tamwick repositioning themselves to be strategic talent resourcing and operational technology consultancy, Specialising in Life Sciences and Data Centres.
Essentially their USP:
They have lots of specialist manufacturing & automation resources that understand the Life Sciences Industry

Competitor websites:
https://vnrhublink.com/ I really like the clarity on this site and the pink/yellow mix could be replaced with a green/blue mix for Tamwick?
https://mrtovex.com/ These are a big company so anything we could steal would be good 😊

They want:
• Fresh, sharp imagery
• Movement on the main page (Rosalind is obsessed with this lol) so may be video on some sections?
• The facility to upload CVs so similar to above.
• A page to show types of jobs available
• A page to show types of resource available from Tamwick
• About us
• Sectors they operate in (includes Life Sciences, Food & Bev, Data Centres)

Target Market(s)

HR/Recruitment/Talent Acquisition/Operations Personnel in Life Sciences and Data Centres

Industry/Entity Type

Life Sciences and Data Centres

Number of Pages Required

1 page

Font styles to use
Sans Serif

Colors
0054AA
0677BA
7BADD7
CADEEF
E8F1F8
0094D4
00A9DD
6FCCEA
C7EBF8
E9F6FB
00AB8E
00BBA5
67D7C9
C6EFE9
E9F9F6

Requirements
Must have
• Brand Colour might be green/blue mix OR if another colour combo compelling
Nice to have
• Fresh, Sharp imagery. Movement on the main image (maybe partial video)

```html
<!DOCTYPE html>
<html lang="en">
<head>
<meta charset="utf-8">
<title>Tamwick — Strategic Talent Resourcing</title>
<link href="https://fonts.googleapis.com/css2?family=Lato:wght@400;700;900&family=Montserrat:wght@400;500;600;700&display=swap" rel="stylesheet">
<style>
:root{
  --teal-deep:#0a5466;
  --teal-head:#0b5c6f;
  --blue-1:#33b4e4;
  --blue-2:#0f7fb9;
  --ink:#1c1c1c;
  --body:#4a4a4a;
  --muted:#6a6a6a;
  --black:#0d0d0d;
  --card-dark:#141414;
  --light:#f4f6f7;
  --line:#e3e6e8;
  --white:#ffffff;
}
*{box-sizing:border-box;margin:0;padding:0}
html,body{width:1200px;height:4342px;overflow:hidden}
body{font-family:"Montserrat",sans-serif;color:var(--ink);background:var(--white);position:relative}
.head-font{font-family:"Lato",sans-serif}
.btn{display:inline-flex;align-items:center;justify-content:center;border-radius:30px;background:linear-gradient(180deg,var(--blue-1),var(--blue-2));color:var(--white);font-weight:700;font-size:11px;letter-spacing:.8px;text-transform:uppercase;box-shadow:0 2px 6px rgba(15,127,185,.35)}
.section-title{font-family:"Lato",sans-serif;font-weight:700;color:var(--teal-head);font-size:27px;text-align:center}

/* Hero */
.hero{position:absolute;left:0;top:0;width:1200px;height:539px;
  background:radial-gradient(ellipse 60% 35% at 55% 38%,rgba(40,160,90,.55),transparent 70%),
  radial-gradient(ellipse 40% 30% at 20% 62%,rgba(30,140,60,.45),transparent 70%),
  linear-gradient(180deg,#0b1a1c 0%,#0e2a22 45%,#0a1a12 75%,#0b0d0c 100%)}
.nav{position:absolute;left:184px;top:0;width:832px;height:52px;display:flex;align-items:center}
.logo{font-family:"Lato",sans-serif;font-weight:900;font-size:25px;color:var(--white)}
.nav-links{margin-left:auto;display:flex;gap:26px;font-size:11px;color:var(--white);align-items:center}
.nav-links .caret{display:inline-block;width:6px;height:6px;border-right:1.5px solid #fff;border-bottom:1.5px solid #fff;transform:rotate(45deg);margin-left:6px;position:relative;top:-2px}
.nav .btn{margin-left:26px;width:92px;height:26px;font-size:9px}
.hero h1{position:absolute;top:160px;width:100%;text-align:center;font-family:"Lato",sans-serif;font-weight:700;font-size:49px;line-height:64px;color:var(--white)}
.hero p{position:absolute;top:300px;width:100%;text-align:center;font-size:13px;color:#e8efe9}
.hero .btn{position:absolute;left:532px;top:352px;width:135px;height:37px}

/* USP */
.usp-photo{position:absolute;left:184px;top:602px;width:367px;height:466px;background:linear-gradient(160deg,#c9c2b8,#8d8b8c 50%,#3a3634)}
.usp-text{position:absolute;left:627px;top:690px;width:388px}
.usp-text h2{font-family:"Lato",sans-serif;font-weight:700;color:var(--teal-head);font-size:27px;margin-bottom:18px}
.usp-text p{font-size:10.5px;line-height:16px;color:var(--body);margin-bottom:11px}
.usp-text p.strong{font-weight:600;color:var(--ink)}
.usp-text .btn{margin-top:14px;width:110px;height:30px;font-size:10px}

/* Team */
.team{position:absolute;left:0;top:1132px;width:1200px;height:1097px;background:linear-gradient(180deg,#e6f6fb 0%,#ffffff 40%,#ffffff 100%)}
.team-intro{position:absolute;left:184px;top:55px;width:600px}
.team-intro h2{font-family:"Lato",sans-serif;font-weight:700;color:var(--teal-head);font-size:27px;margin-bottom:14px}
.team-intro p{font-size:10px;line-height:15px;color:var(--body);margin-bottom:12px}
.team-intro p.strong{font-weight:600;color:var(--ink)}
.team .see-all{position:absolute;left:930px;top:140px;width:86px;height:30px;font-size:10px}
.member{position:absolute;width:263px;height:405px;background:var(--card-dark)}
.member .photo{height:299px}
.member h3{font-family:"Lato",sans-serif;font-weight:700;color:var(--white);font-size:15px;text-align:center;margin-top:20px}
.member .role{font-size:9.5px;letter-spacing:.8px;color:#d9d9d9;text-align:center;margin-top:7px;text-transform:uppercase}
.member .social{display:flex;justify-content:center;gap:13px;margin-top:10px}
.member .social span{width:19px;height:19px;border-radius:50%;background:var(--blue-2);display:block}

/* Stats */
.stats{position:absolute;left:0;top:2229px;width:1200px;height:223px;background:radial-gradient(ellipse 70% 60% at 50% 110%,#1a7a8c,transparent 70%),linear-gradient(180deg,#05505f,#0a5a6c)}
.stat{position:absolute;top:64px;width:200px;text-align:center;color:var(--white)}
.stat .num{font-family:"Lato",sans-serif;font-weight:700;font-size:46px;line-height:52px}
.stat .label{font-size:10px;letter-spacing:.8px;color:#cfe3e8;margin-top:12px;line-height:15px;text-transform:uppercase}

/* Sectors */
.sectors-title{position:absolute;top:2505px;width:1200px}
.sector{position:absolute;top:2580px;width:263px;height:354px}
.sector .name{position:absolute;left:0;bottom:0;width:100%;height:58px;background:rgba(60,60,60,.7);color:var(--white);font-family:"Lato",sans-serif;font-size:21px;display:flex;align-items:center;justify-content:center}

/* Clients */
.clients{position:absolute;left:0;top:2988px;width:1200px;height:239px;background:var(--light)}
.clients .section-title{position:absolute;top:42px;width:100%}
.client{position:absolute;top:101px;width:170px;height:94px;background:var(--white);border:1px solid var(--line);display:flex;align-items:center;justify-content:center;gap:8px;font-family:"Lato",sans-serif;font-weight:700;font-size:17px;color:#3b4a5a}
.client.active{box-shadow:0 6px 18px rgba(0,0,0,.12);border-color:transparent}
.client i{width:10px;height:10px;border-radius:50%;background:#3b4a5a;display:block}
.arrow{position:absolute;top:135px;width:26px;height:26px;border-radius:50%;display:flex;align-items:center;justify-content:center}
.arrow.prev{left:100px;background:var(--white);box-shadow:0 1px 4px rgba(0,0,0,.2)}
.arrow.next{left:1072px;background:var(--teal-deep)}

/* News */
.news-title{position:absolute;top:3280px;width:1200px}
.news{position:absolute;top:3355px;width:263px;height:388px;background:var(--white);border:1px solid var(--line)}
.news.active{box-shadow:0 8px 24px rgba(0,0,0,.12);border-color:transparent}
.news .photo{height:185px}
.news h3{font-family:"Lato",sans-serif;font-weight:400;font-size:15px;line-height:21px;color:var(--ink);margin:22px 20px 10px}
.news p{font-size:9.5px;line-height:14.5px;color:var(--muted);margin:0 20px}
.news .more{position:absolute;left:20px;top:335px;width:104px;height:24px;border-radius:20px;border:1.5px solid var(--blue-2);color:var(--teal-head);font-size:9px;font-weight:700;letter-spacing:.6px;display:flex;align-items:center;justify-content:center;gap:5px}
.news.active .more{background:linear-gradient(180deg,var(--blue-1),var(--blue-2));color:#fff;border-color:transparent}

/* Footer */
.footer{position:absolute;left:0;top:3983px;width:1200px;height:359px;background:var(--black);color:#cfcfcf}
.talk{position:absolute;left:184px;top:3815px;width:832px;height:222px;background:var(--teal-deep);z-index:2}
.talk .photo{position:absolute;left:0;top:0;width:330px;height:222px;background:linear-gradient(120deg,#d9d4c8,#a9a191 55%,#6e6658)}
.talk .copy{position:absolute;left:347px;top:50px;width:460px;color:var(--white)}
.talk h2{font-family:"Lato",sans-serif;font-weight:400;font-size:21px;margin-bottom:14px}
.talk p{font-size:9.5px;line-height:15px;color:#d6e8ec}
.talk .outline{margin-top:18px;width:93px;height:27px;border:1.5px solid #fff;border-radius:20px;display:flex;align-items:center;justify-content:center;font-size:8.5px;font-weight:700;letter-spacing:.6px}
.footer .flogo{position:absolute;left:184px;top:103px;font-family:"Lato",sans-serif;font-weight:900;font-size:40px;color:var(--white)}
.footer .about{position:absolute;left:184px;top:162px;width:280px;font-size:9px;line-height:14px;color:#cfcfcf}
.fcol{position:absolute;top:103px;font-size:9px;line-height:22px}
.fcol h4{font-weight:600;color:var(--white);font-size:10px;margin-bottom:10px}
.contact-row{display:flex;gap:10px;align-items:flex-start;line-height:14px;margin-bottom:12px}
.contact-row svg{flex:none;margin-top:2px}
.footer .copyright{position:absolute;left:184px;top:328px;font-size:9px}
.footer .fsocial{position:absolute;left:936px;top:325px;display:flex;gap:14px}
.footer .fsocial span{width:15px;height:15px;border-radius:3px;background:#e8e8e8;display:block}
</style>
</head>
<body>

<header class="hero">
  <nav class="nav">
    <div class="logo">Tamwick</div>
    <div class="nav-links">
      <span>About</span>
      <span>Capabilities<span class="caret"></span></span>
      <span>Our Clients</span>
      <span>Careers</span>
    </div>
    <span class="btn">Contact Us</span>
  </nav>
  <h1>Strategic Talent Resourcing and<br>Operational Technology Experts</h1>
  <p>Specialising in Life Sciences and Data Centres.</p>
  <span class="btn">Contact Us</span>
</header>

<section aria-label="Our USP">
  <div class="usp-photo" role="img" aria-label="Photo of two engineers smiling beside server equipment with a laptop"></div>
  <div class="usp-text">
    <h2>Our USP</h2>
    <p>Tamwick is proud to be providing top-tier resources to the life sciences sector, specialising in delivering high-quality talent and solutions that enhance the capabilities and operational excellence of our customers.</p>
    <p>Our operational technology expertise and talent pool has evolved over the past decade with successful project delivery for numerous life sciences organisations, so we are uniquely positioned to understand and meet your requirements.</p>
    <p class="strong">We are focused on matching the dynamic needs of life sciences firms with skilled professionals, thereby driving innovation and growth in this critical sector across Ireland.</p>
    <span class="btn">Read More</span>
  </div>
</section>

<section class="team" aria-label="Meet our Team">
  <div class="team-intro">
    <h2>Meet our Team</h2>
    <p>Tamwick employees have a variety of skills and experience, but they all are professional, experienced in their field and enjoy the variety of working at different client sites over time.</p>
    <p class="strong">They get a feeling of success seeing a project through to completion, and are always willing to go the extra mile for our clients.</p>
  </div>
  <span class="btn see-all">See All</span>

  <article class="member" style="left:184px;top:214px">
    <div class="photo" role="img" aria-label="Portrait of a young automation engineer with a laptop" style="background:linear-gradient(180deg,#e9ecef,#b9c6d6 60%,#6d87a8)"></div>
    <h3>Corin Maddock</h3><div class="role">Automation Engineer</div>
    <div class="social"><span></span><span></span><span></span></div>
  </article>
  <article class="member" style="left:468px;top:214px">
    <div class="photo" role="img" aria-label="Portrait of a recruitment specialist in a grey blazer" style="background:linear-gradient(180deg,#eeeae4,#cfc9c1 60%,#8f8c88)"></div>
    <h3>Elspeth Varley</h3><div class="role">Recruitment Specialist</div>
    <div class="social"><span></span><span></span></div>
  </article>
  <article class="member" style="left:753px;top:214px">
    <div class="photo" role="img" aria-label="Portrait of a manufacturing engineer in a hard hat and hi-vis vest" style="background:linear-gradient(180deg,#f1f1ef,#e3e6d8 60%,#c8d98a)"></div>
    <h3>Ines Ratcliffe</h3><div class="role">Manufacturing Engineer</div>
    <div class="social"><span></span><span></span></div>
  </article>
  <article class="member" style="left:184px;top:641px">
    <div class="photo" role="img" aria-label="Portrait of a controls engineer in a dark blazer" style="background:linear-gradient(180deg,#6b5a4c,#3c332d 60%,#1f1f22)"></div>
    <h3>Noreen Gilfoyle</h3><div class="role">Controls Engineer</div>
    <div class="social"><span></span><span></span><span></span></div>
  </article>
  <article class="member" style="left:468px;top:641px">
    <div class="photo" role="img" aria-label="Portrait of a packaging engineer wearing glasses" style="background:linear-gradient(180deg,#e7dccd,#c9b9a4 55%,#9fb7c4)"></div>
    <h3>Tobin Archer</h3><div class="role">Packaging Engineer</div>
    <div class="social"><span></span><span></span><span></span></div>
  </article>
  <article class="member" style="left:753px;top:641px">
    <div class="photo" role="img" aria-label="Portrait of an MES engineer in a striped shirt" style="background:linear-gradient(180deg,#d8d8d6,#bdbdbb 60%,#8a8a8c)"></div>
    <h3>Ravel Dunmore</h3><div class="role">MES Engineer</div>
    <div class="social"><span></span><span></span></div>
  </article>
</section>

<section class="stats" aria-label="Key figures">
  <div class="stat" style="left:223px"><div class="num">50+</div><div class="label">Number skilled automation<br>engineers</div></div>
  <div class="stat" style="left:500px"><div class="num">25+</div><div class="label">Customers currently using Tamwick</div></div>
  <div class="stat" style="left:777px"><div class="num">99%</div><div class="label">Customer retention</div></div>
</section>

<h2 class="section-title sectors-title">Featured Sectors</h2>
<div class="sector" style="left:184px;background:linear-gradient(160deg,#d8d2cc,#9a9491 60%,#5a5a5e)" role="img" aria-label="Microscope and laboratory flasks">
  <div class="name">Life Sciences</div>
</div>
<div class="sector" style="left:468px;background:linear-gradient(160deg,#b9523f,#d8b48c 55%,#8a6b4f)" role="img" aria-label="Table of food and drinks">
  <div class="name">Food and Beverages</div>
</div>
<div class="sector" style="left:753px;background:linear-gradient(100deg,#3a4048,#1e232a 50%,#556070)" role="img" aria-label="Rows of data centre server racks">
  <div class="name">Data Centres</div>
</div>

<section class="clients" aria-label="Client List">
  <h2 class="section-title">Client List</h2>
  <span class="arrow prev"><svg width="12" height="12" viewBox="0 0 12 12"><path d="M10 6H2M5 3L2 6l3 3" stroke="#333" stroke-width="1.5" fill="none"/></svg></span>
  <div class="client" style="left:121px"><i></i>Helvora</div>
  <div class="client" style="left:318px"><i></i>Corrant Biolabs</div>
  <div class="client active" style="left:515px"><i></i>Medrion</div>
  <div class="client" style="left:712px"><i></i>Vellacor</div>
  <div class="client" style="left:909px"><i></i>Stonegrid</div>
  <span class="arrow next"><svg width="12" height="12" viewBox="0 0 12 12"><path d="M2 6h8M7 3l3 3-3 3" stroke="#fff" stroke-width="1.5" fill="none"/></svg></span>
</section>

<h2 class="section-title news-title">Latest News</h2>
<article class="news" style="left:184px">
  <div class="photo" role="img" aria-label="Technician working at a server rack" style="background:linear-gradient(120deg,#d9d5d0,#8c8a8c 55%,#2c2f36)"></div>
  <h3>Posuere amet neque massa urna arcu. Tellus egestas amet lacus neque viverra commodo.</h3>
  <p>Semper amet cursus rhoncus ipsum. Nibh blandit ullamcorper velit non quam faucibus leo sit. Eget nunc malesuada.</p>
  <span class="more">READ MORE <svg width="8" height="8" viewBox="0 0 8 8"><path d="M1 4h6M4.5 1.5L7 4 4.5 6.5" stroke="currentColor" stroke-width="1.2" fill="none"/></svg></span>
</article>
<article class="news active" style="left:468px">
  <div class="photo" role="img" aria-label="Close-up of blue network cables in a patch panel" style="background:linear-gradient(120deg,#1d3f77,#2f6fb5 50%,#17243a)"></div>
  <h3>Ligula non a porttitor nisl quam dictum. Facilisis nisl nisl dui ipsum. Senectus proin egestas.</h3>
  <p>Ultrices arcu lacinia volutpat tristique adipiscing platea viverra. Id justo nullam arcu purus aliquam ultricies mi elit.</p>
  <span class="more">READ MORE <svg width="8" height="8" viewBox="0 0 8 8"><path d="M1 4h6M4.5 1.5L7 4 4.5 6.5" stroke="currentColor" stroke-width="1.2" fill="none"/></svg></span>
</article>
<article class="news" style="left:753px">
  <div class="photo" role="img" aria-label="Engineer on a phone call at a laptop in a server room" style="background:linear-gradient(120deg,#1f3e6a,#3a5e8e 50%,#9aa6b4)"></div>
  <h3>Ipsum ullamcorper amet praesent a. Ornare felis et arcu nam odio. Nunc suspendisse.</h3>
  <p>Malesuada egestas vel amet eu enim sem. Sed a tempor nec dignissim lectus eu. Quam malesuada et vivamus ac.</p>
  <span class="more">READ MORE <svg width="8" height="8" viewBox="0 0 8 8"><path d="M1 4h6M4.5 1.5L7 4 4.5 6.5" stroke="currentColor" stroke-width="1.2" fill="none"/></svg></span>
</article>

<section class="talk" aria-label="Talk to Us">
  <div class="photo" role="img" aria-label="Woman smiling while working on a laptop at a desk"></div>
  <div class="copy">
    <h2>Talk to Us.</h2>
    <p>At convallis sit elit fringilla eget ac ultrices risus. Ac sapien urna morbi sollicitudin adipiscing feugiat pulvinar. Vitae eu id vitae adipiscing elit urna elit morbi odio. Tellus sem sapien dignissim sociis. Malesuada eget quis imperdiet libero a. At.</p>
    <div class="outline">CONTACT US</div>
  </div>
</section>

<footer class="footer">
  <div class="flogo">Tamwick</div>
  <p class="about">Lorem ipsum dolor sit amet consectetur. Amet egestas in at eu non faucibus consequat. Quam eu leo pretium lorem. Neque curabitur arcu ut est nunc fringilla molestie convallis.</p>
  <div class="fcol" style="left:586px">
    <h4>Navigation</h4>
    <div>Home</div><div>About</div><div>Capabilities</div><div>Our Clients</div><div>Careers</div><div>Contact Us</div>
  </div>
  <div class="fcol" style="left:728px">
    <h4>Quick Links</h4>
    <div>Privacy Policy</div><div>Cookie Policy</div><div>Terms &amp; Conditions</div><div>Employee Directory</div><div>FAQ</div>
  </div>
  <div class="fcol" style="left:901px;width:120px">
    <h4>Contact Information</h4>
    <div class="contact-row"><svg width="9" height="11" viewBox="0 0 9 11"><path d="M4.5 10.5S1 6.5 1 4.2a3.5 3.5 0 017 0C8 6.5 4.5 10.5 4.5 10.5z" fill="#2aa8d8"/><circle cx="4.5" cy="4.2" r="1.3" fill="#0d0d0d"/></svg><span>48 Harbour Row,<br>Kelmore, County<br>10422 Ireland</span></div>
    <div class="contact-row"><svg width="10" height="10" viewBox="0 0 10 10"><path d="M2 1l2 2-1 1.3a6 6 0 002.7 2.7L7 6l2 2-1.3 1.3C4.5 9 1 5.5.7 2.3z" fill="#2aa8d8"/></svg><span>+1 555 014 2290</span></div>
    <div class="contact-row"><svg width="10" height="8" viewBox="0 0 10 8"><rect x=".5" y=".5" width="9" height="7" fill="#2aa8d8"/><path d="M.5.5L5 4.5 9.5.5" stroke="#0d0d0d" fill="none"/></svg><span>mail@tamwick.io</span></div>
  </div>
  <div class="copyright">© 2024 Tamwick. All Rights Reserved.</div>
  <div class="fsocial"><span></span><span></span><span></span></div>
</footer>

</body>
</html>
```